owlbrass website

commerce website to sell cookeries, brackets, mailboxes and to show off homes built. Modern Steel in design see tandra wheels web page to be like: https://www.tandrawheels.example/en/ sorry its net haven hosting word press divi

must be able to add products to page

Target Market(s)

mainly western states of U.S.

Industry/Entity Type

Building Product

Coding

Coded - Design and coding required

Number of Pages Required

3 page

Font styles to use
Sans Serif

Colors

Designer to choose colors to be used in the design.

Requirements
Must have
• customers to be able to order products from page
• net haven hosting word press divi

```html
<!DOCTYPE html>
<html lang="en">
<head>
<meta charset="utf-8">
<title>Owl Brass — Steel Products</title>
<link href="https://fonts.googleapis.com/css2?family=Fira+Sans:ital,wght@0,300;0,400;0,500;0,700;0,800;1,500&display=swap" rel="stylesheet">
<style>
:root{
  --header:#445d8b;
  --navy:#1f3050;
  --accent-blue:#3e5a8a;
  --band:#3d5587;
  --news-top:#3f5889;
  --news-bottom:#4a6596;
  --footer:#223352;
  --orange:#f7820f;
  --star:#f0531c;
  --ink:#1d2430;
  --line:#b9bec6;
  --white:#ffffff;
  --font:'Fira Sans', sans-serif;
}
*{margin:0;padding:0;box-sizing:border-box}
html,body{width:1200px;height:2296px;overflow:hidden}
body{position:relative;font-family:var(--font);background:var(--white);color:var(--ink)}
.abs{position:absolute}

/* header */
.topbar{left:0;top:0;width:1200px;height:72px;background:var(--header)}
.brand{left:158px;top:20px;color:var(--white);font-size:22px;font-weight:500;letter-spacing:.5px;display:flex;align-items:center;gap:8px}
.brand .dot{width:26px;height:26px;border-radius:50%;border:2px solid var(--white)}
.brand b{font-weight:700}
.search{left:382px;top:16px;width:361px;height:40px;background:var(--white);border-radius:2px;display:flex;align-items:center;padding-left:13px;font-size:13px;color:#8a8f98;letter-spacing:.6px}
.search .sep{position:absolute;right:46px;top:8px;width:1px;height:24px;background:#c7ccd3}
.search svg{position:absolute;right:14px;top:10px}
.account{top:28px;color:var(--white);font-size:14px;font-weight:500;display:flex;align-items:center;gap:6px}

/* nav */
.nav{left:158px;top:72px;width:884px;height:42px;background:var(--white);display:flex;align-items:center;padding-left:47px;font-size:14px;font-weight:500;color:var(--ink);letter-spacing:.3px}
.nav span.slash{margin:0 27px}
.lang{left:870px;top:87px;font-size:14px;font-weight:500}
.lang-sep{left:933px;top:82px;width:1px;height:22px;background:#ccd}
.social-top{top:80px;width:28px;height:28px;border:1.5px solid var(--accent-blue);border-radius:50%;color:var(--accent-blue);font-size:8px;font-weight:500;display:flex;align-items:center;justify-content:center}

/* hero */
.hero{left:0;top:114px;width:1200px;height:448px;background:var(--navy);overflow:hidden}
.hero-bold{left:156px;top:178px;color:var(--white);font-size:72px;line-height:72px;font-weight:800;letter-spacing:1px}
.hero-light{left:156px;top:250px;color:var(--white);font-size:64px;line-height:64px;font-weight:300;letter-spacing:9px}
.hero-sub{left:159px;top:321px;color:var(--white);font-size:22px;line-height:27px;font-weight:400}
.hero-text{left:158px;top:384px;color:#dfe4ec;font-size:14px;line-height:23px;font-weight:300}
.btn-shop{left:158px;top:447px;width:134px;height:42px;background:var(--white);color:var(--ink);font-size:13px;font-weight:700;display:flex;align-items:center;justify-content:center;border-radius:2px}
.slider-bar{left:461px;top:521px;width:282px;height:41px;background:var(--orange);display:flex;align-items:center;justify-content:center;gap:6px}
.slider-bar i{width:9px;height:9px;border-radius:50%;background:var(--white);display:block}
.slider-bar i.on{background:var(--accent-blue);border:2px solid var(--white)}
.slider-bar .track{width:78px;height:1px;background:var(--white);margin-left:10px}

/* categories */
.card{top:593px;height:282px;background:var(--white);box-shadow:0 1px 4px rgba(0,0,0,.25);padding:3px}
.card .photo{width:100%;height:237px}
.card .label{height:42px;background:var(--band);color:var(--white);font-size:20px;font-weight:700;display:flex;align-items:center;justify-content:space-between;padding:0 14px}

/* testimonial */
.rule{height:1.5px;background:var(--line)}
.quote-badge{left:572px;top:938px;width:56px;height:56px;border-radius:50%;background:var(--white);box-shadow:0 1px 4px rgba(0,0,0,.2);display:flex;align-items:center;justify-content:center}
.stars{left:0;width:1200px;top:1014px;text-align:center;color:var(--star);font-size:20px;letter-spacing:2px}
.quote{left:230px;width:740px;top:1051px;text-align:center;font-size:18.5px;line-height:27.5px;font-style:italic;font-weight:500;color:#3c424c;text-transform:uppercase}
.author{left:0;width:1200px;top:1182px;text-align:center;color:var(--accent-blue);font-size:17px;font-weight:500}
.author-role{left:0;width:1200px;top:1210px;text-align:center;color:#7a8088;font-size:13px;letter-spacing:1px}
.btn-reviews{left:411px;top:1259px;width:378px;height:45px;background:linear-gradient(#3e5788,#2d4470);color:var(--white);font-size:14px;font-weight:700;display:flex;align-items:center;justify-content:center;border-radius:2px}

/* newsletter */
.news-band{left:0;top:1400px;width:1200px;height:319px;background:linear-gradient(180deg,var(--news-top),var(--news-bottom))}
.news-title{left:0;width:1200px;top:1494px;text-align:center;color:var(--white);font-size:40px;font-weight:700;letter-spacing:-.5px}
.news-sub{left:0;width:1200px;top:1547px;text-align:center;color:var(--white);font-size:21px;font-weight:400}
.news-input{left:312px;top:1605px;width:398px;height:42px;background:var(--white);border-radius:2px;display:flex;align-items:center;gap:8px;padding-left:10px;font-size:15px;color:#6d737c;letter-spacing:.4px}
.news-btn{left:716px;top:1605px;width:172px;height:42px;background:var(--orange);color:var(--white);font-size:18px;font-weight:700;display:flex;align-items:center;justify-content:center;border-radius:2px}

/* footer */
.footer{left:0;top:1719px;width:1200px;height:577px;background:var(--footer)}
.footer-brand{left:158px;top:1860px;color:var(--white);font-size:28px;font-weight:500;display:flex;align-items:center;gap:10px}
.footer-brand .dot{width:34px;height:34px;border-radius:50%;border:2px solid var(--white)}
.contact{left:158px;color:var(--white);font-size:14px;line-height:22px;display:flex;gap:12px}
.contact svg{flex:none;margin-top:2px}
.col-head{top:1874px;color:var(--white);font-size:20px;font-weight:700}
.col-links{top:1932px;color:var(--white);font-size:14px;line-height:33px;letter-spacing:.3px}
.col-sep{top:1881px;width:1px;height:201px;background:#4a5b7a}
.copy{left:158px;top:2187px;color:var(--white);font-size:12px}
.social-foot{top:2173px;width:43px;height:43px;border:1.5px solid var(--white);border-radius:50%;color:var(--white);font-size:11px;font-weight:500;display:flex;align-items:center;justify-content:center}
.pay{top:2185px;color:var(--white);font-size:13px;font-weight:500}
.pay-main{font-size:22px;font-weight:700}
</style>
</head>
<body>

<!-- header -->
<div class="abs topbar"></div>
<div class="abs brand"><span class="dot"></span><span><b>OWL</b> BRASS</span></div>
<div class="abs search">Enter your key words...
  <span class="sep"></span>
  <svg width="20" height="20" viewBox="0 0 20 20"><circle cx="8" cy="8" r="6.5" fill="none" stroke="#2d4470" stroke-width="2"/><line x1="13" y1="13" x2="18" y2="18" stroke="#2d4470" stroke-width="2.2"/></svg>
</div>
<div class="abs account" style="left:803px">
  <svg width="18" height="14" viewBox="0 0 18 14"><rect x="1" y="3" width="12" height="10" fill="none" stroke="#fff" stroke-width="1.5"/><rect x="6" y="1" width="11" height="8" fill="#fff"/></svg>REGISTER</div>
<div class="abs account" style="left:899px">
  <svg width="12" height="13" viewBox="0 0 12 13"><circle cx="6" cy="4" r="3" fill="#fff"/><path d="M1 13c0-4 2-5 5-5s5 1 5 5z" fill="#fff"/></svg>LOG IN</div>
<div class="abs account" style="left:984px;top:24px">
  <svg width="28" height="26" viewBox="0 0 28 26"><path d="M1 3h4l3 13h14l3-9H8" fill="none" stroke="#fff" stroke-width="2"/><circle cx="11" cy="21" r="2" fill="#fff"/><circle cx="20" cy="21" r="2" fill="#fff"/><text x="14" y="9" fill="#fff" font-size="9" font-family="Fira Sans, sans-serif">0</text></svg>Cart</div>

<!-- nav -->
<div class="abs nav">Home<span class="slash">/</span>Products<span class="slash">/</span>Homes Built<span class="slash">/</span>About<span class="slash">/</span>Contact</div>
<div class="abs lang">En ◐ ▾</div>
<div class="abs lang-sep"></div>
<div class="abs social-top" style="left:949px">Nook</div>
<div class="abs social-top" style="left:982px">Flit</div>
<div class="abs social-top" style="left:1014px">Lumo</div>

<!-- hero -->
<div class="abs hero">
  <svg width="1200" height="448" viewBox="0 0 1200 448" style="position:absolute;left:0;top:0">
    <defs>
      <linearGradient id="heroPhoto" x1="0" y1="0" x2="1" y2="0">
        <stop offset="0" stop-color="#4c5a5e"/>
        <stop offset=".3" stop-color="#2c2f33"/>
        <stop offset=".65" stop-color="#3a3b3d"/>
        <stop offset="1" stop-color="#6a6561"/>
      </linearGradient>
    </defs>
    <polygon points="457,0 526,0 571,131 440,340" fill="var(--accent-blue)"/>
    <g role="img" aria-label="Photo of a steel-clad building with glass entrance doors">
      <polygon points="526,0 1200,0 1200,448 440,448 571,131" fill="url(#heroPhoto)"/>
    </g>
    <polygon points="378,448 408,341 490,448" fill="var(--accent-blue)"/>
  </svg>
</div>
<div class="abs hero-bold">OWL</div>
<div class="abs hero-light">BRASS</div>
<div class="abs hero-sub">Aenean eget risusut<br>risus porttitor</div>
<div class="abs hero-text">Tulla lobortis neque sit amet enim<br>pharetra, quis consectetur libero lacinia.</div>
<div class="abs btn-shop">SHOP PRODUCTS</div>
<div class="abs slider-bar"><i class="on"></i><i></i><i></i><i></i><span class="track"></span></div>

<!-- categories -->
<div class="abs card" style="left:158px;width:283px">
  <div class="photo" role="img" aria-label="Photo of black steel pots and pans" style="background:radial-gradient(circle at 50% 55%,#6d6d6d,#2a2a2a)"></div>
  <div class="label">STEEL COOKERY<span>⟶</span></div>
</div>
<div class="abs card" style="left:458px;width:284px">
  <div class="photo" role="img" aria-label="Photo of galvanized steel brackets" style="background:radial-gradient(circle at 50% 50%,#b8bcc0,#f1f2f3)"></div>
  <div class="label">BRACKETS<span>⟶</span></div>
</div>
<div class="abs card" style="left:758px;width:284px">
  <div class="photo" role="img" aria-label="Photo of a red and white steel mailbox" style="background:linear-gradient(90deg,#7a7468,#d94545 45%,#e8e8e8 60%,#4f6b3c)"></div>
  <div class="label">MAILBOXES<span>⟶</span></div>
</div>

<!-- testimonial -->
<div class="abs rule" style="left:158px;top:965px;width:884px"></div>
<div class="abs quote-badge">
  <svg width="34" height="22" viewBox="0 0 34 22"><path d="M2 11a8 8 0 0 1 14-5c0 7-5 13-12 14 3-2 5-5 5-7a7 7 0 0 1-7-2z" fill="#3f4550"/><path d="M18 11a8 8 0 0 1 14-5c0 7-5 13-12 14 3-2 5-5 5-7a7 7 0 0 1-7-2z" fill="#3f4550"/></svg>
</div>
<div class="abs stars">★★★★★</div>
<div class="abs quote">Praesent felis diam, sagittis vitae urna vel, ornare molestie neque. Nam libero magna, interdum quis elementum tempus, auctor eget augue. Fusce varius orci tortor, in rhoncus nunc mollis quis. Duis vulputate commodo bibendum. Cras ultrices, mauris sed consectetur molestie.</div>
<div class="abs author">QUISQUE SED ELIT DIGNISSIM,</div>
<div class="abs author-role">SEMPER JUSTO QUIS</div>
<div class="abs rule" style="left:158px;top:1280px;width:884px"></div>
<div class="abs btn-reviews">READ MORE ABOUT WHAT PEOPLE SAYS</div>

<!-- newsletter -->
<div class="abs news-band" role="img" aria-label="Blue faceted steel texture background"></div>
<div class="abs news-title">JOIN OUR NEWSLETTER NOW</div>
<div class="abs news-sub">Get E-mail updates about our latest shop and special offers.</div>
<div class="abs news-input">
  <svg width="14" height="10" viewBox="0 0 14 10"><rect x=".5" y=".5" width="13" height="9" fill="none" stroke="#aab"/><path d="M.5 .5l6.5 5 6.5-5" fill="none" stroke="#aab"/></svg>Enter your mail id</div>
<div class="abs news-btn">Subscribe Now</div>

<!-- footer -->
<div class="abs footer"></div>
<div class="abs footer-brand"><span class="dot"></span><span><b>OWL</b> BRASS</span></div>

<div class="abs contact" style="top:1932px">
  <svg width="14" height="18" viewBox="0 0 14 18"><path d="M7 1a6 6 0 0 1 6 6c0 4-6 10-6 10S1 11 1 7a6 6 0 0 1 6-6z" fill="var(--orange)"/><circle cx="7" cy="7" r="2.2" fill="var(--footer)"/></svg>
  <div>4820 Copperline Road<br>Boise ID, USA</div></div>
<div class="abs contact" style="top:1986px">
  <svg width="14" height="14" viewBox="0 0 14 14"><rect x="1" y="3" width="12" height="9" fill="none" stroke="var(--orange)" stroke-width="1.6"/><path d="M1 3l6 5 6-5" fill="none" stroke="var(--orange)" stroke-width="1.6"/></svg>
  <div>hello@owlbrass.example<br>We reply within 24 hours</div></div>
<div class="abs contact" style="top:2042px">
  <svg width="14" height="18" viewBox="0 0 14 18"><path d="M6 2c-3 1-4 5-3 8s3 6 6 7l2-3-3-2-1 1c-1-1-2-3-2-5l1-1-1-4z" fill="var(--orange)"/></svg>
  <div>(208) 555 0147<br>Mon-Fri, 9am until 6pm</div></div>

<div class="abs col-sep" style="left:393px"></div>
<div class="abs col-sep" style="left:609px"></div>
<div class="abs col-sep" style="left:830px"></div>

<div class="abs col-head" style="left:432px">INFOMATION</div>
<div class="abs col-links" style="left:434px">About Us<br>Contact Us<br>FAQs<br>Privacy Policy<br>Terms &amp; Conditions</div>
<div class="abs col-head" style="left:649px">HELP</div>
<div class="abs col-links" style="left:651px">FAQs<br>Orders and Returns<br>Shipping Policies<br>International Shipping<br>Term &amp; Conditions</div>
<div class="abs col-head" style="left:871px">YOUR ACCOUNT</div>
<div class="abs col-links" style="left:873px">Cart<br>Checkout<br>My account<br>Contact<br>Privacy Policy</div>

<div class="abs rule" style="left:158px;top:2144px;width:884px;height:1px;background:#7d8aa3"></div>
<div class="abs copy">© 2020 Owl Brass. All rights reserved.</div>
<div class="abs social-foot" style="left:528px">Nook</div>
<div class="abs social-foot" style="left:578px">Flit</div>
<div class="abs social-foot" style="left:628px">Lumo</div>
<div class="abs pay pay-main" style="left:760px;top:2179px">PayRiver</div>
<div class="abs pay" style="left:866px">Orbit</div>
<div class="abs pay" style="left:910px">Vanta</div>
<div class="abs pay" style="left:955px">Corvex</div>
<div class="abs pay" style="left:1002px">Meridia</div>

</body>
</html>
```